Business card for our start up Automotive Shop

Clean business card design for our new automotive shop Brightline Motor Works. This card will be the template for all of our staff member including technicians and service advisors.

Brightline Motor Works is an automotive service shop catering to US domestic and asian import vehicles. We are a service and maintenance full service facility. Our aim is to provide the best quality workmanship and the best customer service experience in our industry.

Our target market are young professionals to people with families. We are not targeting a younger audience or the car modification scene. The card should be appealing to women of the 30+ age demographic.

We are a shop of younger professionals instead of an older crowd. The card design should reflect as such.

Target Market(s)

30+ Female demographic and 30+ male.

Industry/Entity Type

Automotive

Contact Information for Business Card

Must be clean and appealing to clients. Large enough and easy to read print.

Font styles to use
Sans Serif

Colors
f78f20
ffffff
b2b2b2
dddddd

Requirements
Must have
• Address, website and phone number
• 42-15 58th Ave
• Cedar Hollow NY 11462
• (718) 402-3917
• brightlinemotorworks.com
• There must be an area to add a Name and e-mail address for personalization purposes.
Nice to have
• Back of the card should have website.
• I would also like to incorporate yelp, google+, Facebook, and instagram widgets. Will add the exact pages but everything can be @ or / brightlinemotorworks
• That can be added on the back of the card.

```html
<!DOCTYPE html>
<html lang="en">
<head>
<meta charset="utf-8">
<title>Brightline Motor Works – Business Card</title>
<link rel="stylesheet" href="https://fonts.googleapis.com/css2?family=Lato:wght@400;700&display=swap">
<style>
  :root {
    --orange: #f78f20;
    --white: #ffffff;
    --grey: #b2b2b2;
    --light-grey: #dddddd;
    --ink: #222222;
    --stage: #efefef;
    --band-text: #f6b2a8;
  }
  * { box-sizing: border-box; margin: 0; padding: 0; }
  html, body { width: 1200px; height: 586px; overflow: hidden; }
  body {
    position: relative;
    background: var(--stage);
    font-family: "Lato", sans-serif;
  }
  .card {
    position: absolute;
    top: 128px;
    width: 500px;
    height: 300px;
    border-radius: 16px;
    background: var(--white);
    overflow: hidden;
  }
  .card--front { left: 62px; }
  .card--back { left: 619px; }

  /* Front */
  .floral-side {
    position: absolute; left: 0; top: 0;
    width: 178px; height: 300px;
    background: linear-gradient(90deg, rgba(247,143,32,0.55) 0%, rgba(247,143,32,0.3) 60%, rgba(247,143,32,0) 100%);
  }
  .floral-faint {
    position: absolute; right: 0; top: 0;
    width: 170px; height: 300px;
    background: linear-gradient(270deg, rgba(247,143,32,0.12) 0%, rgba(247,143,32,0) 100%);
  }
  .brand-mark {
    position: absolute; left: 208px; top: 102px;
    display: flex; align-items: center; gap: 10px;
  }
  .brand-mark__dot {
    width: 44px; height: 44px; border-radius: 50%;
    background: var(--orange);
    flex: none;
  }
  .brand-mark__name {
    color: var(--orange);
    font-weight: 700;
    font-size: 22px;
    line-height: 1.05;
    width: 150px;
  }
  .social {
    position: absolute; left: 297px; top: 232px;
    display: flex; gap: 4px;
  }
  .social__dot {
    width: 27px; height: 27px; border-radius: 50%;
    background: var(--orange);
  }
  .social-handle {
    position: absolute; left: 257px; top: 267px; width: 200px;
    text-align: center;
    color: var(--orange);
    font-size: 12px;
  }

  /* Back */
  .brand-line {
    position: absolute; left: 31px; top: 32px;
    display: flex; align-items: center; gap: 8px;
  }
  .brand-line__dot {
    width: 34px; height: 34px; border-radius: 50%;
    background: var(--orange);
  }
  .brand-line__name {
    color: var(--orange);
    font-weight: 700;
    font-size: 16px;
    letter-spacing: 0.5px;
    border-left: 1px solid var(--grey);
    padding-left: 8px;
    line-height: 34px;
  }
  .person {
    position: absolute; right: 26px; top: 34px;
    text-align: right;
  }
  .person__name { color: var(--orange); font-weight: 700; font-size: 15px; }
  .person__role { color: var(--ink); font-size: 11px; margin-top: 5px; }
  .contact {
    position: absolute; right: 26px; top: 94px;
    list-style: none;
  }
  .contact__item {
    display: flex; justify-content: flex-end; align-items: center;
    gap: 9px; height: 24px;
    color: var(--ink); font-size: 12px;
  }
  .contact__icon { width: 16px; height: 16px; flex: none; }
  .address {
    position: absolute; right: 26px; top: 181px;
    text-align: right;
    color: var(--orange); font-weight: 700; font-size: 12px; line-height: 16px;
  }
  .swirl {
    position: absolute; left: 0; top: 148px;
    width: 270px; height: 81px;
    background: linear-gradient(0deg, rgba(247,143,32,0.28) 0%, rgba(247,143,32,0) 100%);
  }
  .band {
    position: absolute; left: 0; top: 229px;
    width: 500px; height: 60px;
    background: var(--orange);
  }
  .band__web {
    position: absolute; left: 295px; top: 11px;
    color: var(--band-text);
    font-size: 11px; letter-spacing: 1.6px;
  }
</style>
</head>
<body>

  <section class="card card--front" aria-label="Card back">
    <div class="floral-side" role="img" aria-label="Orange floral swirl ornament"></div>
    <div class="floral-faint" role="img" aria-label="Faint pale orange floral ornament"></div>
    <div class="brand-mark">
      <span class="brand-mark__dot"></span>
      <span class="brand-mark__name">Brightline Motor Works</span>
    </div>
    <div class="social" aria-label="Social pages">
      <span class="social__dot"></span>
      <span class="social__dot"></span>
      <span class="social__dot"></span>
      <span class="social__dot"></span>
    </div>
    <p class="social-handle">/brightlinemotorworks</p>
  </section>

  <section class="card card--back" aria-label="Card front">
    <div class="brand-line">
      <span class="brand-line__dot"></span>
      <span class="brand-line__name">BRIGHTLINE MOTOR WORKS</span>
    </div>

    <div class="person">
      <p class="person__name">Dana Whitfield</p>
      <p class="person__role">Northgate Advisors</p>
    </div>

    <ul class="contact">
      <li class="contact__item">(718) 402-3917
        <svg class="contact__icon" viewBox="0 0 16 16" aria-hidden="true">
          <circle cx="8" cy="8" r="8" fill="var(--orange)"/>
          <path d="M4 6.2c0-1 1.8-1.9 4-1.9s4 .9 4 1.9v.8h-2v-.9H6v.9H4z M5 8h6l.8 3.5H4.2z" fill="var(--white)"/>
        </svg>
      </li>
      <li class="contact__item">dwhitfield@brightlinemotorworks.com
        <svg class="contact__icon" viewBox="0 0 16 16" aria-hidden="true">
          <circle cx="8" cy="8" r="8" fill="var(--orange)"/>
          <rect x="4" y="5" width="8" height="6" fill="var(--white)"/>
          <path d="M4 5l4 3.3L12 5" fill="none" stroke="var(--orange)" stroke-width="0.9"/>
        </svg>
      </li>
      <li class="contact__item">www.brightlinemotorworks.com
        <svg class="contact__icon" viewBox="0 0 16 16" aria-hidden="true">
          <circle cx="8" cy="8" r="8" fill="var(--orange)"/>
          <circle cx="8" cy="8" r="4" fill="none" stroke="var(--white)" stroke-width="1"/>
          <ellipse cx="8" cy="8" rx="1.8" ry="4" fill="none" stroke="var(--white)" stroke-width="0.9"/>
          <path d="M4 8h8" stroke="var(--white)" stroke-width="0.9"/>
        </svg>
      </li>
    </ul>

    <p class="address">42-15 58th Ave<br>Cedar Hollow NY 11462</p>

    <div class="swirl" role="img" aria-label="Orange swirl and leaf ornament rising from the band"></div>
    <div class="band">
      <span class="band__web">www.brightlinemotorworks.com</span>
    </div>
  </section>

</body>
</html>
```